New Dental Office Needs an Attractive and user friendly Website Designed

I need a website for a new dental office. The Name is Maplecrest Dentistry. I would like a Modern design with a user friendly interface and usability.
I would like a landing page, a page that lists the services we offer: Cosmetic Dentistry, Implants, Dental Hygiene, Emergency Services, Restorations, Dentures
Target Market(s)
Mid to upper class
Industry/Entity Type
Dentistry
Coding
Coded - Design and coding required
Number of Pages Required
1 page
Requirements
Must have
- Landing page that has a scheduling option, Procedures, operating hours, and contact us info
Nice to have
- Appealing design, Soft comforting colors. Easy to navigate page, Modern and professional.

```html
<!DOCTYPE html>
<html lang="en">
<head>
<meta charset="UTF-8">
<title>Maplecrest Dentistry</title>
<link rel="stylesheet" href="https://fonts.googleapis.com/css2?family=Merriweather:wght@400;700&family=Poppins:wght@400;500;600&display=swap">
<style>
:root{
  --teal:#6ad6c6;
  --orange:#ee7d52;
  --ink:#333333;
  --muted:#6f6f6f;
  --mint:#e2f6f2;
  --peach:#fbe1d7;
  --cream:#fdf8ea;
  --gray:#f6f6f6;
  --line:#e3e3e3;
  --star:#f5b400;
}
*{box-sizing:border-box;margin:0;padding:0}
html,body{width:1200px;height:4295px;overflow:hidden}
body{position:relative;font-family:"Poppins",sans-serif;color:var(--ink);background:#fff}
.serif{font-family:"Merriweather",serif}
section,footer{position:absolute;left:0;width:1200px;overflow:hidden}
.abs{position:absolute}
.btn{position:absolute;display:flex;align-items:center;justify-content:center;border-radius:30px;color:#fff;font-weight:600;font-size:14px;text-transform:uppercase;letter-spacing:.3px}
.btn-teal{background:var(--teal)}
.btn-orange{background:var(--orange)}
.accent{color:var(--teal)}
.photo{position:absolute}

/* hero */
.hero{top:0;height:1283px;background:var(--mint)}
.brand{position:absolute;font-family:"Merriweather",serif;font-weight:700;color:var(--ink)}
.hero .brand{left:88px;top:36px;font-size:23px}
.nav{position:absolute;top:41px;left:0;font-size:12px;font-weight:500;text-transform:uppercase}
.nav span{position:absolute;white-space:nowrap;color:var(--ink)}
.nav .active{color:var(--teal)}
.hero-photo{left:590px;top:118px;width:570px;height:700px;border-radius:285px 285px 0 0;background:linear-gradient(160deg,#e8b9a3 0%,#d49a86 45%,#f3d5c5 100%)}
.hero-wave{position:absolute;left:0;top:0}
.hero-title{left:103px;top:208px;font-size:56px;line-height:70px;font-weight:700;width:520px;z-index:2}
.hero-sub{left:104px;top:446px;font-size:15px;color:#666}
.features-title{left:0;width:1200px;top:845px;text-align:center;color:#fff;font-size:31px;font-weight:400}
.feature{position:absolute;width:240px;text-align:center;color:#fff}
.ring{width:140px;height:140px;margin:0 auto;border-radius:50%;background:rgba(255,255,255,.35);display:flex;align-items:center;justify-content:center}
.ring.active{background:var(--orange)}
.ring .core{width:116px;height:116px;border-radius:50%;background:#fff;display:flex;align-items:center;justify-content:center}
.feature h3{font-family:"Merriweather",serif;font-weight:400;font-size:20px;line-height:27px;margin-top:32px}
.feature p{font-size:14px;line-height:20px;margin-top:8px}

/* services */
.services{top:1283px;height:677px;background:#fff}
.services-photo{left:125px;top:100px;width:463px;height:512px;border-radius:48% 0 50% 50%/42% 0 50% 50%;background:linear-gradient(150deg,#9fb1c4 0%,#3e5a86 45%,#d9b394 80%,#e9e1d6 100%);box-shadow:0 18px 30px rgba(0,0,0,.12)}
.services-title{left:653px;top:148px;width:470px;font-size:32px;line-height:46px;font-weight:400}
.services-lead{left:653px;top:257px;width:440px;font-size:14px;line-height:22px;color:var(--muted)}
.service-list{position:absolute;left:653px;top:301px;width:424px;list-style:none}
.service-list li{height:51px;display:flex;align-items:center;justify-content:space-between;border-bottom:1px solid var(--line);font-family:"Merriweather",serif;font-size:15px}
.service-list li:last-child{border-bottom:none}
.arrow-dot{width:28px;height:28px;border-radius:50%;background:var(--orange);display:flex;align-items:center;justify-content:center;margin-right:12px}
.view-all{left:654px;top:535px;font-size:14px;font-weight:600;color:var(--teal);text-decoration:underline;text-transform:uppercase}

/* ready + dentist */
.ready{top:1960px;height:898px;background:var(--mint)}
.ready-cap{position:absolute;left:0;top:0}
.ready-title{left:0;width:1200px;top:24px;text-align:center;font-size:46px;font-weight:700}
.ready-sub{left:0;width:1200px;top:95px;text-align:center;font-size:18px;color:#666}
.dentist-title{left:162px;top:440px;font-size:33px;line-height:44px;font-weight:400}
.dentist-text{left:162px;top:507px;width:455px;font-size:13px;line-height:22px;color:var(--muted)}
.quote-box{left:163px;top:637px;width:432px;height:73px;background:#fff;border-left:5px solid var(--orange);border-radius:8px;padding:14px 20px;font-size:14px;line-height:22px;color:#555;box-shadow:0 6px 16px rgba(0,0,0,.05)}
.arch{left:713px;top:382px;width:405px;height:516px;border-radius:203px 203px 0 0;background:var(--peach)}
.dentist-photo{left:760px;top:305px;width:330px;height:593px;border-radius:165px 165px 0 0;background:linear-gradient(180deg,#d8b39c 0%,#c89b82 22%,#5fb6d9 40%,#3d9ccb 100%)}

/* testimonials */
.reviews{top:2858px;height:562px;background:#fff}
.reviews-title{left:0;width:1200px;top:97px;text-align:center;font-size:32px;font-weight:400}
.reviews-sub{left:230px;width:740px;top:150px;text-align:center;font-size:13px;line-height:22px;color:#555}
.card{position:absolute;top:259px;width:328px;height:200px;background:#fff;border-radius:10px;box-shadow:0 8px 28px rgba(0,0,0,.08)}
.avatar{position:absolute;left:36px;top:-34px;width:68px;height:68px;border-radius:50%;border:3px solid #fff;background:linear-gradient(160deg,#c9a48e,#4d6a8c);box-shadow:0 4px 10px rgba(0,0,0,.1)}
.card .mark{position:absolute;left:180px;top:-2px;font-family:"Merriweather",serif;font-size:110px;line-height:1;color:rgba(238,125,82,.2);font-weight:700}
.card p{position:absolute;left:27px;top:62px;width:280px;font-size:12.5px;line-height:20px;color:#666}
.card .name{position:absolute;left:27px;top:163px;font-size:13px;font-weight:600}
.card .stars{position:absolute;right:27px;top:160px;font-size:14px;color:var(--star);letter-spacing:1px}
.dots{position:absolute;left:576px;top:508px;display:flex;gap:8px}
.dots i{width:8px;height:8px;border-radius:50%;background:#d5d5d5}
.dots i.on{background:var(--teal)}

/* contact */
.contact{top:3420px;height:510px;background:#fff}
.contact-bg{position:absolute;left:0;top:0}
.contact-card{left:165px;top:27px;width:868px;height:420px;background:#fff;border-radius:22px;box-shadow:0 10px 40px rgba(0,0,0,.08)}
.contact-panel{left:408px;top:10px;width:450px;height:400px;background:var(--cream);border-radius:14px}
.field{position:absolute;background:#f4f4f4;border-radius:28px;font-size:13px;color:#666;padding:0 28px;display:flex;align-items:center}
.contact-title{left:463px;top:103px;font-size:30px;line-height:42px;font-weight:400}
.contact-lead{left:463px;top:205px;width:360px;font-size:14px;line-height:23px;color:var(--muted)}

/* footer */
.site-footer{top:3930px;height:365px;background:var(--gray)}
.site-footer .brand{left:88px;top:80px;font-size:36px;line-height:48px}
.col{position:absolute;top:62px}
.col h4{font-family:"Merriweather",serif;font-size:15px;font-weight:700;margin-bottom:14px}
.col a,.col p{display:block;font-size:13px;line-height:25px;color:#555;text-decoration:none}
.hours-row{display:flex;gap:8px;font-size:13px;line-height:20px;color:#555;margin-bottom:8px}
.hours-row svg{margin-top:3px;flex:none}
.news-input{position:absolute;left:0;top:75px;width:233px;height:46px;border-radius:23px;background:#ebebeb;display:flex;align-items:center;padding:0 18px;font-size:12px;color:#777;gap:8px}
.news-input .send{margin-left:auto}
.rule{left:70px;top:312px;width:1060px;height:1px;background:#dcdcdc}
.copyright{left:0;width:1200px;top:324px;text-align:center;font-size:12px;color:#555}
.to-top{left:1133px;top:293px;width:50px;height:50px;border-radius:50%;background:var(--orange);display:flex;align-items:center;justify-content:center}
</style>
</head>
<body>

<section class="hero">
  <div class="photo hero-photo" role="img" aria-label="Smiling young woman with braces, arms crossed"></div>
  <svg class="hero-wave" width="1200" height="1283" viewBox="0 0 1200 1283" aria-hidden="true">
    <path d="M0,572 Q600,1030 1200,548 L1200,1283 L0,1283 Z" fill="#ee7d52"/>
    <path d="M0,555 Q600,1000 1200,530 L1200,1283 L0,1283 Z" fill="#6ad6c6"/>
  </svg>
  <div class="brand">Maplecrest Dentistry</div>
  <nav class="nav">
    <span class="active" style="left:503px">Home</span>
    <span style="left:567px">About Us</span>
    <span style="left:657px">Services</span>
    <span style="left:743px">New Patients</span>
    <span style="left:860px">Contact</span>
  </nav>
  <div class="btn btn-orange" style="left:957px;top:30px;width:153px;height:38px;font-size:11px">Book Appointment</div>

  <h1 class="abs serif hero-title">Smile Brighter With <span class="accent">Maplecrest</span> Dentistry</h1>
  <p class="abs hero-sub">Modern Care. Gentle Touch. Personalized for You.</p>
  <div class="btn btn-teal" style="left:107px;top:500px;width:230px;height:50px">Schedule Your Visit</div>
  <div class="btn btn-orange" style="left:348px;top:500px;width:144px;height:50px">Call Now</div>

  <h2 class="abs serif features-title">Exceptional Care, Beautiful Results</h2>

  <div class="feature" style="left:107px;top:923px">
    <div class="ring"><div class="core">
      <svg width="52" height="52" viewBox="0 0 52 52" fill="none" stroke="#ee7d52" stroke-width="2"><circle cx="26" cy="22" r="8"/><path d="M12 46c0-9 6-14 14-14s14 5 14 14"/><path d="M26 4l1.5 3 3 .5-2.2 2 .6 3-2.9-1.5-2.9 1.5.6-3-2.2-2 3-.5z"/><path d="M12 10l1 2 2 .3-1.5 1.4.4 2-1.9-1-1.9 1 .4-2L9 12.3l2-.3z"/><path d="M40 10l1 2 2 .3-1.5 1.4.4 2-1.9-1-1.9 1 .4-2-1.5-1.4 2-.3z"/></svg>
    </div></div>
    <h3>Experienced<br>Dentists</h3>
  </div>
  <div class="feature" style="left:358px;top:977px">
    <div class="ring"><div class="core">
      <svg width="52" height="52" viewBox="0 0 52 52" fill="none" stroke="#ee7d52" stroke-width="2"><circle cx="26" cy="20" r="10"/><path d="M16 18c2-7 18-7 20 0"/><path d="M10 46c0-9 7-14 16-14s16 5 16 14"/><path d="M22 32l4 6 4-6"/></svg>
    </div></div>
    <h3>Patient-Centered<br>Approach</h3>
  </div>
  <div class="feature" style="left:602px;top:923px">
    <div class="ring active"><div class="core">
      <svg width="52" height="52" viewBox="0 0 52 52" fill="none" stroke="#ee7d52" stroke-width="2"><path d="M16 10c-6 0-9 5-8 11 1 5 3 8 4 13 1 6 2 12 5 12 3 0 3-10 9-10s6 10 9 10c3 0 4-6 5-12 1-5 3-8 4-13 1-6-2-11-8-11-4 0-6 2-10 2s-6-2-10-2z"/><path d="M42 6l1 3 3 1-3 1-1 3-1-3-3-1 3-1z"/></svg>
    </div></div>
    <h3>Advanced<br>Technology</h3>
    <p>Precision tools for<br>modern care</p>
  </div>
  <div class="feature" style="left:855px;top:977px">
    <div class="ring"><div class="core">
      <svg width="52" height="52" viewBox="0 0 52 52" fill="none" stroke="#ee7d52" stroke-width="2"><circle cx="26" cy="26" r="19"/><circle cx="26" cy="26" r="14"/><path d="M26 17v9l6 4"/></svg>
    </div></div>
    <h3>Flexible<br>Scheduling</h3>
  </div>
</section>

<section class="services">
  <div class="photo services-photo" role="img" aria-label="Dentist in blue scrubs treating a patient in the clinic chair"></div>
  <h2 class="abs serif services-title">Comprehensive Dental Services Under One Roof</h2>
  <p class="abs services-lead">Feel free to get in touch with Maplecrest dentistry Clinic for general dentistry, specialist treatments or facial aesthetics.</p>
  <ul class="service-list">
    <li>Cosmetic Dentistry<span class="arrow-dot"><svg width="12" height="12" viewBox="0 0 12 12" fill="none" stroke="#fff" stroke-width="1.6"><path d="M3 9l6-6M4 3h5v5"/></svg></span></li>
    <li>Dental Implants<span class="arrow-dot"><svg width="12" height="12" viewBox="0 0 12 12" fill="none" stroke="#fff" stroke-width="1.6"><path d="M3 9l6-6M4 3h5v5"/></svg></span></li>
    <li>Dental Hygiene &amp; Cleanings<span class="arrow-dot"><svg width="12" height="12" viewBox="0 0 12 12" fill="none" stroke="#fff" stroke-width="1.6"><path d="M3 9l6-6M4 3h5v5"/></svg></span></li>
    <li>Emergency Dentistry<span class="arrow-dot"><svg width="12" height="12" viewBox="0 0 12 12" fill="none" stroke="#fff" stroke-width="1.6"><path d="M3 9l6-6M4 3h5v5"/></svg></span></li>
  </ul>
  <span class="abs view-all">View All Services</span>
</section>

<section class="ready">
  <svg class="ready-cap" width="1200" height="340" viewBox="0 0 1200 340" aria-hidden="true">
    <path d="M0,0 H1200 V40 Q600,560 0,62 Z" fill="#ee7d52"/>
    <path d="M0,0 H1200 V48 Q600,520 0,65 Z" fill="#ffffff"/>
  </svg>
  <h2 class="abs serif ready-title">Ready to <span class="accent">Prioritize</span> Your Smile?</h2>
  <p class="abs ready-sub">Booking your visit is quick and easy. New patients welcome!</p>
  <div class="btn btn-teal" style="left:468px;top:140px;width:265px;height:48px">Book Appointment Now</div>

  <h2 class="abs serif dentist-title">Meet Your Dentist</h2>
  <p class="abs dentist-text">Dr. Reed is dedicated to providing personalized, gentle, and compassionate dental care. With years of experience and a passion for patient comfort, Dr. Reed ensures every visit is a positive experience. Whether it's your routine check-up or a more complex procedure, you'll feel at ease knowing you're in expert hands.</p>
  <div class="abs quote-box">“My goal is to make every patient feel at home while receiving the highest quality care.”</div>
  <div class="btn btn-teal" style="left:163px;top:728px;width:302px;height:49px">Learn More About Our Team</div>
  <div class="abs arch"></div>
  <div class="photo dentist-photo" role="img" aria-label="Smiling male dentist in light blue scrubs with arms crossed"></div>
</section>

<section class="reviews">
  <h2 class="abs serif reviews-title">What Our <span class="accent">Patients Are Saying</span></h2>
  <p class="abs reviews-sub">It is a long established fact that a reader will be distracted by the readable content of a page when looking at its layout. The point of using Lorem Ipsum is that it has a more-or-less normal.</p>
  <div class="card" style="left:92px">
    <div class="avatar" role="img" aria-label="Patient portrait"></div>
    <span class="mark">“</span>
    <p>It is a long established fact that a reader will be distracted by the readable content of a page when looking at its layout. The point of using Lorem Ipsum is that it has a...</p>
    <span class="name">– Sarah M.</span><span class="stars">★★★★★</span>
  </div>
  <div class="card" style="left:437px">
    <div class="avatar" role="img" aria-label="Patient portrait"></div>
    <span class="mark">“</span>
    <p>It is a long established fact that a reader will be distracted by the readable content of a page when looking at its layout. The point of using Lorem Ipsum is that it has a...</p>
    <span class="name">– Tom R.</span><span class="stars">★★★★★</span>
  </div>
  <div class="card" style="left:782px">
    <div class="avatar" role="img" aria-label="Patient portrait"></div>
    <span class="mark">“</span>
    <p>It is a long established fact that a reader will be distracted by the readable content of a page when looking at its layout. The point of using Lorem Ipsum is that it has a...</p>
    <span class="name">— Presley S. —</span><span class="stars">★★★★★</span>
  </div>
  <div class="dots"><i></i><i class="on"></i><i></i></div>
</section>

<section class="contact">
  <svg class="contact-bg" width="1200" height="510" viewBox="0 0 1200 510" aria-hidden="true">
    <path d="M0,225 Q600,670 1200,238 L1200,510 L0,510 Z" fill="#f6f6f6"/>
    <path d="M0,225 Q600,670 1200,238" fill="none" stroke="#ee7d52" stroke-width="6"/>
  </svg>
  <div class="abs contact-card">
    <div class="abs contact-panel"></div>
    <div class="field" style="left:35px;top:31px;width:175px;height:55px">First Name*</div>
    <div class="field" style="left:218px;top:31px;width:167px;height:55px">Last Name*</div>
    <div class="field" style="left:35px;top:103px;width:175px;height:55px">Email*</div>
    <div class="field" style="left:218px;top:103px;width:167px;height:55px">Phone*</div>
    <div class="field" style="left:35px;top:170px;width:350px;height:143px;border-radius:20px;align-items:flex-start;padding-top:16px">Send Your Message*</div>
    <div class="btn btn-teal" style="left:137px;top:333px;width:143px;height:48px">Submit</div>
    <h2 class="abs serif contact-title">Have a Question?<br>We’re Happy to Help.</h2>
    <p class="abs contact-lead">Feel free to get in touch with Maplecrest dentistry Clinic for general dentistry, specialist treatments or facial aesthetics.</p>
    <div class="btn btn-teal" style="left:463px;top:286px;width:144px;height:50px">Call Now</div>
  </div>
</section>

<footer class="site-footer">
  <div class="brand">Maplecrest<br>Dentistry</div>
  <div class="col" style="left:473px">
    <h4>Quick Links</h4>
    <a>Home</a><a>About Us</a><a>Services</a><a>New Patients</a><a>Contact</a>
  </div>
  <div class="col" style="left:658px">
    <h4>Operating Hours</h4>
    <div class="hours-row"><svg width="12" height="12" viewBox="0 0 12 12"><circle cx="6" cy="6" r="6" fill="#ee7d52"/><path d="M6 3v3l2 1.5" stroke="#fff" stroke-width="1.3" fill="none"/></svg><span>Mon – Fri :<br>8:00 AM – 6:00 PM</span></div>
    <div class="hours-row"><svg width="12" height="12" viewBox="0 0 12 12"><circle cx="6" cy="6" r="6" fill="#ee7d52"/><path d="M6 3v3l2 1.5" stroke="#fff" stroke-width="1.3" fill="none"/></svg><span>Saturday :<br>9:00 AM – 2:00 PM</span></div>
    <div class="hours-row" style="padding-left:20px"><span>Sunday :<br><u>Closed</u></span></div>
  </div>
  <div class="col" style="left:877px;width:240px">
    <h4>Newsletter</h4>
    <p style="line-height:20px">Subscribe to our email address to get the latest news.</p>
    <div class="news-input">
      <svg width="13" height="10" viewBox="0 0 13 10"><rect width="13" height="10" rx="1.5" fill="#ee7d52"/><path d="M1 1.5l5.5 4 5.5-4" stroke="#fff" fill="none"/></svg>
      Enter Your Email...
      <svg class="send" width="16" height="16" viewBox="0 0 16 16"><path d="M1 7.5L15 1 10 15 7.5 9z" fill="#ee7d52"/></svg>
    </div>
  </div>
  <div class="abs rule"></div>
  <p class="abs copyright">© copyright 2025 Maplecrest Dentistry. All Rights Reserved.</p>
  <div class="abs to-top"><svg width="14" height="10" viewBox="0 0 14 10" fill="none" stroke="#fff" stroke-width="2"><path d="M2 8l5-5 5 5"/></svg></div>
</footer>

</body>
</html>
```